I need a label with logo to go on jars of honey.
Label size 70mm x 70mm
The front label should say :
The Tall Fern Honey Co. (logo)
Tarepo Honey
400g
The back label:
Would have nutritional information
And our address
You can see from the uploaded files the styles I prefer, I have uploaded a photo of the honey product too. The background of the logo doesn't have to be white. I would like to develop a color scheme that would look nice against the color of the honey.
Logo Text
The Tall Fern Honey Co. / The Tall Fern Honey Company

```html
<!DOCTYPE html>
<html lang="en">
<head>
<meta charset="utf-8">
<title>The Tall Fern Honey Company – Jar Labels</title>
<link rel="stylesheet" href="https://fonts.googleapis.com/css2?family=Montserrat:wght@500&family=Open+Sans:wght@400;600&display=swap">
<style>
  :root {
    --honey-gold: #daa522;
    --label-paper: #f1f1f1;
    --ink: #1c1c1c;
    --page: #ffffff;
  }
  * { margin: 0; padding: 0; box-sizing: border-box; }
  html, body {
    width: 1200px; height: 865px; overflow: hidden;
    background: var(--page);
  }
  .canvas { position: relative; width: 1200px; height: 865px; }

  /* Front label */
  .front-label {
    position: absolute; left: 0; top: 0;
    width: 722px; height: 865px;
    background: var(--label-paper);
    border: 18px solid var(--honey-gold);
  }
  .brand-mark {
    position: absolute; border-radius: 50%;
    background: var(--honey-gold);
  }
  .front-label .brand-mark { left: 226px; top: 47px; width: 220px; height: 220px; }

  .wordmark {
    position: absolute; text-align: center;
    font-family: "Montserrat", sans-serif; font-weight: 500;
    color: var(--ink); text-transform: uppercase; white-space: nowrap;
  }
  .front-label .wordmark { left: 0; width: 686px; top: 326px; }
  .front-label .wordmark-name { display: block; font-size: 38px; letter-spacing: 0.17em; line-height: 50px; }
  .front-label .wordmark-sub { display: block; font-size: 22px; letter-spacing: 1.45em; line-height: 30px; margin-top: 6px; padding-left: 1.45em; }

  .product-band {
    position: absolute; left: 97px; top: 526px;
    width: 493px; height: 188px;
    background: var(--honey-gold);
    display: flex; align-items: center; justify-content: center;
  }
  .product-name {
    font-family: "Open Sans", sans-serif; font-weight: 600;
    font-size: 64px; letter-spacing: -0.01em; color: var(--ink);
  }
  .net-weight {
    position: absolute; left: 0; width: 686px; top: 750px;
    text-align: center;
    font-family: "Open Sans", sans-serif; font-weight: 400;
    font-size: 50px; color: var(--ink);
  }

  /* Back label */
  .back-label {
    position: absolute; left: 808px; top: 154px;
    width: 392px; height: 555px;
    background: var(--label-paper);
  }
  .section-title {
    position: absolute;
    font-family: "Montserrat", sans-serif; font-weight: 500;
    color: var(--ink); text-transform: uppercase; white-space: nowrap;
  }
  .nutrition-title { left: 24px; top: 57px; font-size: 16px; letter-spacing: 0.36em; }
  .bracket { position: absolute; overflow: visible; }
  .nutrition-panel { left: 20px; top: 95px; width: 353px; height: 178px; }
  .back-label .brand-mark { left: 22px; top: 331px; width: 191px; height: 191px; }
  .address-title { left: 252px; top: 384px; font-size: 14px; letter-spacing: 0.3em; }
  .address-panel { left: 243px; top: 390px; width: 128px; height: 108px; }
  .back-label .wordmark { left: 190px; width: 190px; top: 505px; }
  .back-label .wordmark-name { display: block; font-size: 13px; letter-spacing: 0.12em; line-height: 16px; }
  .back-label .wordmark-sub { display: block; font-size: 8px; letter-spacing: 1.2em; line-height: 12px; padding-left: 1.2em; margin-top: 2px; }
</style>
</head>
<body>
<main class="canvas">
  <section class="front-label" aria-label="Front label">
    <div class="brand-mark" aria-hidden="true"></div>
    <h1 class="wordmark">
      <span class="wordmark-name">The Tall Fern Honey</span>
      <span class="wordmark-sub">Company</span>
    </h1>
    <div class="product-band">
      <p class="product-name">Tarepo Honey</p>
    </div>
    <p class="net-weight">400g</p>
  </section>

  <section class="back-label" aria-label="Back label">
    <h2 class="section-title nutrition-title">Nutritional Information</h2>
    <svg class="bracket nutrition-panel" viewBox="0 0 353 178" aria-hidden="true">
      <polyline points="2,0 2,176 351,176 351,0" fill="none" stroke="var(--honey-gold)" stroke-width="4"/>
    </svg>
    <div class="brand-mark" aria-hidden="true"></div>
    <h2 class="section-title address-title">Address</h2>
    <svg class="bracket address-panel" viewBox="0 0 128 108" aria-hidden="true">
      <polyline points="2,0 2,106 126,106 126,0" fill="none" stroke="var(--honey-gold)" stroke-width="4"/>
    </svg>
    <p class="wordmark">
      <span class="wordmark-name">The Tall Fern Honey</span>
      <span class="wordmark-sub">Company</span>
    </p>
  </section>
</main>
</body>
</html>
```